Speisekarte für Pizzeria
Zielgruppe
Hallo in die Runde,
Wir würden gerne für unser Restaurant / Pizzeria eine neue Speisekarte haben.
Wir sind im höchsten Skigebiet Österreichs umgeben von Bergen und Schnee
am besten könnte ich es euch vorstellen bei einer Drohnen-Aufnahme die ihr unter folgendem Link sehen könnt:
www.firnblick.ag/panorama
Aufgabenstellung
Wir würden gerne ein quadratisches Format haben - 300x300mm
Der Druck sollte auf www.presswerk.at erfolgen
4 Umschlagseiten und 4 Kernseiten
Als Anhang hab ich euch meine jetzige Speisekarte drangehängt...diese ist lediglich im A4 Format und einfach eine klassische Speisekarte.
Nachtrag: weil da einige Fragen aufgekommen sind: die neue Karte sollte alle Speisen sowie auch alle Pizze und Getränke enthalten. Und auf der letzte Seite sollte irgendwie Werbung für unsere Appartments und unseren Wellness-Bereich gemacht werden. Foto gibt es unter www.almrosen.at ... wenn wir dann beim Finalisieren sind, kann ich die Fotos gerne in guter Qualität nachreichen
Wir haben bei uns im Haus auch Appartments mit Wellness Bereich und diese Gäste kommen natürlich auch ins Restaurnt. Weiters kommen aber natürlich auch Gäste aus anderen umliegenden Hotels / Betrieben...um diesen Gästen einen Anreiz zu schaffen, in Zukunft bei uns ihren Urlaub zu verbringen, würde ich gerne auf der letzten Seite unser Hotel bewerben...vielleicht mit einigen Fotos vom Schwimmbad / Ruheraum etc.
Wir haben hier auf dieser Plattform bereits einmal erfolgreich unsere Pizzakartons machen lassen... ein Foto von diesen habe ich auch drangehängt...aber das Design zu übernehmen ist kein Muss !
In unserer jetzigen Speisekarte sind nicht alle Spirituosen angeführt...dort sollte man vielleicht etwas mehr Platz einrechnen, damit ich alle Longdrinks etc. anführen kann. Dies würde ich dann aber erst gerne nachreichen wenn wir mal ein Design haben.

```html
<!DOCTYPE html>
<html lang="de">
<head>
<meta charset="utf-8">
<title>Alma's Speisekarte – Seitenübersicht</title>
<link href="https://fonts.googleapis.com/css2?family=Merriweather:ital,wght@0,400;0,700;1,700&display=swap" rel="stylesheet">
<style>
:root{
  --brown:#6b5343;
  --brown-dark:#5a4537;
  --red:#ee4545;
  --cream:#f4ece2;
  --ink:#4a3a30;
  --grey-bg:#a9a9a9;
  --yellow:#f6c945;
  --paper:#ffffff;
}
*{margin:0;padding:0;box-sizing:border-box}
html,body{width:1021px;height:1200px;overflow:hidden}
body{
  background:radial-gradient(ellipse at 50% 30%,#c4c4c4 0%,#a3a3a3 55%,#8d8d8d 100%);
  font-family:'Merriweather',Georgia,serif;color:var(--ink);position:relative;
}
.page{position:absolute;width:265px;height:265px;background:var(--paper);box-shadow:0 2px 6px rgba(0,0,0,.25);overflow:hidden}
.frame{position:absolute;inset:5px;border:.6px solid var(--brown);pointer-events:none}
.abs{position:absolute}
.photo{position:absolute;border-radius:8px}
.round{border-radius:50%}
h2{font-weight:400;font-size:11px;color:var(--brown);line-height:1.1}
.rule{border-bottom:.6px solid var(--brown);padding-bottom:2px;margin-bottom:5px}
.item{margin-bottom:4px}
.item b{display:block;font-size:5px;color:var(--brown);font-weight:400;line-height:1.2}
.item span{display:block;font-size:3.6px;line-height:1.3;color:#555}
.item i{display:block;font-size:3.6px;font-style:normal;color:#555}
.row{display:flex;justify-content:space-between}
.card{position:absolute;background:#f2f2f2;border-radius:8px;padding:5px 6px}
.box-red{position:absolute;background:var(--red);color:#fff;border-radius:7px}
.box-brown{position:absolute;background:var(--brown);color:#fff;border-radius:7px}
.box-red .item b,.box-red .item span,.box-red .item i,
.box-brown .item b,.box-brown .item span,.box-brown .item i{color:#fff}
.leaf{display:inline-block;width:4px;height:3px;background:#7cb342;border-radius:0 3px 0 3px;margin-left:2px;vertical-align:middle}
.cols{position:absolute;display:flex;gap:10px}
.cols>div{flex:1}
.kid{position:absolute;width:73px;height:42px;background:var(--brown);border-radius:4px;padding:4px 5px}
.kid b{display:block;color:var(--yellow);font-size:5.2px;font-weight:400;line-height:1.15}
.kid span{display:block;color:#fff;font-size:3.8px;line-height:1.3}
.fig{position:absolute;border-radius:40%}
.dessert .item{margin-bottom:3.2px}
</style>
</head>
<body>

<!-- Seite 1: Titel -->
<section class="page" style="left:98px;top:51px">
  <div class="frame"></div>
  <div class="abs" style="left:0;right:0;top:60px;text-align:center;font-size:42px;color:var(--brown);letter-spacing:1px">ALMA'S</div>
  <p class="abs" style="left:0;right:0;top:157px;text-align:center;font-size:10.5px;line-height:1.38;color:var(--ink)">Alma's Team,<br>heisst Sie herzlich Willkommen<br>und wünscht Ihnen einen</p>
  <div class="abs" style="left:55px;top:207px;width:156px;height:28px;background:var(--red);border-radius:4px;color:#fff;font-style:italic;font-weight:700;font-size:17px;text-align:center;line-height:28px">Guten Appetit !</div>
</section>

<!-- Seite 2: Lieblingsspeisen -->
<section class="page" style="left:378px;top:51px">
  <div class="frame"></div>
  <div class="abs" role="img" aria-label="Handgeschriebener Schriftzug Familienrezept – Liebe, Leben, Lachen" style="left:22px;top:14px;width:100px;height:56px;background:#f1eeeb;border-radius:4px"></div>
  <div class="abs" style="left:0;top:82px;width:127px;height:37px;background:var(--red);border-radius:0 5px 5px 0;color:#fff;font-size:11.5px;line-height:1.05;padding:6px 0 0 18px">Die beliebtesten<br>Speisen von:</div>
  <div class="card" style="left:139px;top:12px;width:115px;height:109px">
    <div style="font-style:italic;font-weight:700;font-size:8px;color:var(--brown)">den Kindern Toni &amp; Lisi</div>
    <div class="row" style="font-size:4.6px;color:var(--ink)"><span>Hausgemachtes Tiramisu</span><span>€ 9,90</span></div>
    <div style="font-size:3.3px;color:#777">- Das perfekte Dessert -</div>
    <div class="photo" role="img" aria-label="Foto: Stück Tiramisu auf weißem Teller" style="left:8px;top:34px;width:100px;height:70px;background:radial-gradient(ellipse at 50% 45%,#c7975f 0%,#e9d9c1 45%,#f2f2f2 75%)"></div>
  </div>
  <div class="card" style="left:13px;top:128px;width:114px;height:127px">
    <div style="font-style:italic;font-weight:700;font-size:8px;color:var(--brown)">Sophie</div>
    <div class="row" style="font-size:4.6px"><span>Carpaccio mit Trüffel-<br>Spaghettini</span><span>€ 29,90</span></div>
    <div style="font-size:3.3px;color:#666">ein original sizilianisches Rezept verfeinert<br>mit Rucola &amp; Parmesan</div>
    <div class="photo" role="img" aria-label="Foto: Carpaccio mit Spaghettini und Rucola" style="left:0;top:52px;width:114px;height:75px;background:radial-gradient(ellipse at 55% 45%,#e6d3a8 0%,#c86a55 40%,#b65140 70%,#f2f2f2 95%)"></div>
  </div>
  <div class="card" style="left:139px;top:128px;width:115px;height:127px">
    <div style="font-style:italic;font-weight:700;font-size:8px;color:var(--brown)">Markus</div>
    <div class="row" style="font-size:4.6px"><span>Sepp's Fischsuppe</span><span>€ 32,90</span></div>
    <div style="font-size:3.3px;color:#666">Tomaten-Safransuppe mit Karotten / Fenchel<br>Sellerie / Zucchini, erlesene Fischfilets, Muscheln,<br>Meeresfrüchten, Aioli dazu hausgemachtes<br>Knoblauchbrot</div>
    <div class="photo" role="img" aria-label="Foto: Fischsuppe mit Garnelen in weißer Schale" style="left:6px;top:55px;width:104px;height:72px;background:radial-gradient(ellipse at 50% 60%,#f07a3e 0%,#ee9a62 45%,#f4f4f4 80%)"></div>
  </div>
</section>

<!-- Seite 3: Vorspeisen, Suppen, Salate -->
<section class="page" style="left:657px;top:51px">
  <div class="frame"></div>
  <div class="box-brown" style="left:16px;top:14px;width:117px;height:230px;padding:7px 8px">
    <h2 class="rule" style="color:var(--yellow);border-color:#fff">Vorspeisen</h2>
    <div class="item"><b>Carpaccio vom Tiroler Weiderind, Trüffelcreme, Parmesansplitter, hausgemachtes Brot</b><i>€ 20,90</i></div>
    <div class="item"><b>Tartar von der Roten Beete &amp; Avocado mit Wakame Alge, Wasabi-Schaum und hausgemachtem Brot<span class="leaf"></span></b><i>€ 16,90</i></div>
    <div class="item"><b>Vitello Tonnato rosa Kalbfleisch-Scheiben, Thunfischcreme, Rucola, Tomaten-Pesto, Kapern, hausgemachtes Brot</b><i>€ 20,90</i></div>
    <div class="abs" role="img" aria-label="Foto: belegtes Roastbeef-Sandwich" style="left:2px;top:124px;width:113px;height:100px;border-radius:6px;background:linear-gradient(160deg,#9c6d48 0%,#b07a5c 35%,#c9888a 55%,#e0a94a 75%,#5a4537 100%)"></div>
  </div>
  <div class="abs" style="left:141px;top:14px;width:112px">
    <h2 class="rule">Suppen</h2>
    <div class="item"><b>Tomatencremesuppe Basilikum / Croutons (auch vegan möglich)<span class="leaf"></span></b><i>€ 7,20</i></div>
    <div class="item"><b>Karamellisierte Zwiebelsuppe<span class="leaf"></span> im Tontopf serviert mit Käse-Crouton</b><i>€ 7,50</i></div>
    <div class="item"><b>Rindssuppe mit Kräuter-Frittaten</b><i>€ 6,50</i></div>
    <h2 class="rule" style="margin-top:8px">Salate</h2>
    <div class="item"><b>gemischter Salat &nbsp; € 8,40<span class="leaf"></span></b></div>
    <div class="item"><b>Cesar Salat</b><span>Das Original / Parmesansplitter /Croutons</span>
      <span>▸ ohne Beilag<span class="leaf"></span> € 8,40</span><span>▸ mit gegrillter Hühnerbrust € 23,90</span><span>▸ mit Knoblauch-Garnelen € 29,90</span></div>
    <div class="item"><b>Winter - Bowl<span class="leaf"></span></b><span>Blattsalate / Granatapfelkerne / Schafskäse / Kirschtomaten Bulgur / Parmesanchips / Pinienkerne / rote Zwiebel / Gurken</span><i>€ 17,90</i></div>
  </div>
</section>

<!-- Seite 4: Beilagen, Pasta -->
<section class="page" style="left:98px;top:329px">
  <div class="frame"></div>
  <div class="box-red" style="left:14px;top:14px;width:236px;height:107px;padding:9px 10px">
    <div style="font-size:10.5px;line-height:1.1;margin-bottom:6px">Zu allen Salaten<br>empfehlen wir:</div>
    <div class="item"><b>▸ Knoblauchbaguette mit<br>&nbsp;&nbsp;hausgemachtem Brot</b><i>&nbsp;&nbsp;€ 6,50</i></div>
    <div class="item"><b>▸ Brotkorb</b><i>&nbsp;&nbsp;€ 5,00</i></div>
    <div class="item"><b>▸ Pizzabrot</b><i>&nbsp;&nbsp;€ 8,80</i></div>
    <div class="abs" role="img" aria-label="Foto: geröstetes Knoblauchbaguette" style="left:100px;top:-5px;width:140px;height:110px;border-radius:40%;background:radial-gradient(ellipse at 50% 50%,#f2d16b 0%,#e7b24d 50%,rgba(238,69,69,0) 75%)"></div>
  </div>
  <h2 class="abs rule" style="left:25px;top:133px;width:220px">Pasta / Fisch &amp; mehr</h2>
  <div class="cols" style="left:25px;top:155px;width:222px">
    <div>
      <div class="item"><b>Hausgemachte Schlutzkrapfen<span class="leaf"></span></b><span>Teigtaschen gefüllt mit Topfen &amp; Spinat serviert mit Parmesan &amp; brauner Butter</span><i>3 Stück € 14,50</i><i>6 Stück € 26,90</i></div>
      <div class="item"><b>Spaghetti al Chef</b><span>Garnelen / Kirschtomaten / Zucchinistreifen / Knoblauch Kräuter / Olivenöl</span><i>€ 27,90</i></div>
      <div class="item"><b>Spaghetti Bolognese</b><i>€ 16,90</i></div>
    </div>
    <div>
      <div class="item"><b>Spaghetti Pesto<span class="leaf"></span></b><span>Basilikum / Knoblauch / Olivenöl/ Pinienkerne / Parmesan</span><i>€ 16,50</i></div>
      <div class="item"><b>Saiblingsfilet</b><span>Kross gebraten aus Ötztaler Gewässern Tagliatelle / Fenchel / Lauch / Zitrone / Spinatblätter / Tomatenflocken</span><i>€ 31,20</i></div>
      <div class="item"><b>Carpaccio mit Trüffel-Spaghettini</b><span>ein original sizilianisches Rezept verfeinert mit Rucola &amp; Parmesan</span><i>€ 29,90</i></div>
    </div>
  </div>
</section>

<!-- Seite 5: Holzkohlegrill -->
<section class="page" style="left:378px;top:329px">
  <div class="frame"></div>
  <div class="abs" style="left:17px;top:17px"><h2 style="font-size:10px">Aus dem Holzkohlegrill</h2><div style="font-size:6px;color:var(--brown)">bei offenem Feuer und 350°</div></div>
  <div class="photo" role="img" aria-label="Foto: Steak auf glühendem Holzkohlegrill" style="left:133px;top:13px;width:118px;height:110px;background:radial-gradient(ellipse at 45% 55%,#7a4a33 0%,#3a2a22 40%,#c0451e 85%,#2a1c16 100%)"></div>
  <div class="box-red" style="left:16px;top:48px;width:104px;height:72px;padding:5px 8px">
    <div class="item"><b>Surf &amp; Turf</b><span>200g heimisches Rinderfilet und Jumbo Garnelen</span><i>€ 49,90</i></div>
    <div class="item"><b>Filetsteak <span style="display:inline;font-size:3.6px">ca. 250g</span></b><i>€ 43,90</i></div>
    <div class="item"><b>Holzfällersteak</b><span>vom Kräuterschwein Speck / Zwiebel / Pilze</span><i>€ 28,90</i></div>
  </div>
  <div class="abs" style="left:16px;top:128px;width:104px;height:23px;border:.7px solid var(--red);border-radius:4px;padding:3px 5px">
    <div style="font-size:5px;color:var(--red)">Alle drei servieren wir mit</div>
    <div style="font-size:3.6px;color:#555">Gemüse / Pommes frites / 2 kalte Saucen / Kräuterbutter</div>
  </div>
  <div class="item abs" style="left:17px;top:156px;width:105px"><b>Tagliata</b><span>ca. 250g vom Rumpsteak in Streifen geschnitten dazu Rucola Kirschtomaten / Parmesan / Knoblauchbrot</span><i>€ 34,90</i></div>
  <div class="photo round" role="img" aria-label="Foto: Tagliata mit Rucola auf schwarzem Teller" style="left:18px;top:182px;width:114px;height:73px;background:radial-gradient(ellipse at 50% 50%,#a0483b 0%,#6d3a2c 45%,#1e1a18 70%)"></div>
  <div class="card" style="left:133px;top:130px;width:117px;height:122px;padding:6px 9px">
    <div style="font-size:6.5px;color:var(--brown);line-height:1.2">Saftige hausgemachte Ripperl Sous vide gegart und im Grill verfeinert</div>
    <div style="font-size:3.8px;color:#555;margin-top:3px">am Brettl serviert / 2 Saucen / Folienkartoffel mit Dip und Knoblauchbaguette</div>
    <div style="font-size:3.8px;color:#555">€ 29,90</div>
    <div class="abs" style="left:91px;top:-4px;transform:rotate(25deg);border:.8px solid var(--red);color:var(--red);font-size:5px;font-weight:700;padding:1px 3px;border-radius:2px">TIPP!</div>
    <div class="abs" role="img" aria-label="Foto: glasierte Spareribs" style="left:10px;top:52px;width:105px;height:68px;border-radius:30%;background:radial-gradient(ellipse at 50% 50%,#8a3a1e 0%,#6b2c16 45%,rgba(242,242,242,0) 75%)"></div>
  </div>
</section>

<!-- Seite 6: Hauptspeisen -->
<section class="page" style="left:657px;top:329px">
  <div class="frame"></div>
  <h2 class="abs rule" style="left:18px;right:18px;top:16px;text-align:center">Hauptspeisen</h2>
  <div class="cols" style="left:18px;top:40px;width:230px;gap:12px">
    <div>
      <div class="item"><b>Wiener Schnitzel vom Schwein mit Pommes frites und Preiselbeeren oder mit</b><span>200g heimisches Rinderfilet und Jumbo Garnelen</span><i>€ 19,90</i></div>
      <div class="item"><b>Schlössl Burger</b><span>ca. 100g Rindfleisch mit Cheddarkäse gratiniert, Bacon, Gurken, rote Zwiebel, Tomaten, Salat, zweierlei Sauce und Pommes frites</span><i>€ 16,50</i></div>
      <div class="item"><b>Stollenburger</b><span>200g Rindfleisch (2 Patties) mit Cheddarkäse gratiniert, Bacon, Gurken, Salat, Zwiebel-Marmelade, Tomaten, Spiegelei zweierlei Saucen &amp; Pommes Frites</span><i>€ 20,90</i></div>
    </div>
    <div>
      <div class="item"><b>Veganer Burger<span class="leaf"></span></b><span>Veganes Patty / Tomate / Salat / rote Zwiebel / Wakame Alge Limetten-Aioli und Pommes frites</span><i>€ 19,50</i></div>
      <div class="item"><b>Sepp's Fischsuppeklare</b><span>Tomaten-Safransuppe mit Gemüse, verschiedenen Fischfilets, Muscheln, Meeresfrüchten, Aioli - dazu Knoblauchbrot</span><i>€ 32,90</i></div>
      <div class="item"><b>Garnelen im Tontopf</b><span>250g Black Tiger Garnelen / Knoblauch / Kräuter / bestes Olivenöl hausgemachtes Aioli &amp; Brot zum Dippen</span><i>€ 28,50</i></div>
    </div>
  </div>
  <div class="photo" role="img" aria-label="Foto: Schüsseln mit Currys, Reis und Chilis" style="left:16px;top:163px;width:233px;height:86px;background:linear-gradient(90deg,#3a2418 0%,#d9822d 30%,#e7a33d 50%,#c9532a 75%,#2f1d14 100%)"></div>
</section>

<!-- Seite 7: Pizze -->
<section class="page" style="left:98px;top:607px">
  <div class="frame"></div>
  <h2 class="abs rule" style="left:18px;top:16px;width:105px">Unsere Pizze</h2>
  <div class="abs" style="left:18px;top:40px;width:106px">
    <div class="item"><div class="row"><b>Margherita</b><i>€ 11,90</i></div><span>Tomatensauce, Mozzarella, Basilikum, Olivenöl</span></div>
    <div class="item"><div class="row"><b>Salami</b><i>€ 14,50</i></div><span>Tomatensauce, Mozzarella, Salami, Parmesan, Olivenöl</span></div>
    <div class="item"><div class="row"><b>Funghi</b><i>€ 14,50</i></div><span>Tomatensauce, Mozzarella, Basilikum, Olivenöl</span></div>
    <div class="item"><div class="row"><b>Prosciutto</b><i>€ 14,50</i></div><span>Tomatensauce, Mozzarella, Schinken, Basilikum, Olivenöl</span></div>
    <div class="item"><div class="row"><b>Prosciutto e Funghi</b><i>€ 14,50</i></div><span>Tomatensauce, Mozzarella, frische Champignon, Schinken, Olivenöl</span></div>
    <div class="item"><div class="row"><b>Prosciutto e Salami</b><i>€ 14,50</i></div><span>Tomatensauce, Mozzarella, Salami, Schinken, Olivenöl</span></div>
    <div class="item"><div class="row"><b>Tonno</b><i>€ 14,90</i></div><span>Tomatensauce, Mozzarella, Thunfisch, Oregano, Olivenöl</span></div>
    <div class="item"><div class="row"><b>Tonno e Cipolla</b><i>€ 14,90</i></div><span>Tomatensauce, Mozzarella, Thunfisch, Zwiebel, Oregano</span></div>
    <div class="item"><div class="row"><b>Napoli</b><i>€ 14,90</i></div><span>Tomatensauce, Mozzarella, Sardellen, Kapern, Oregano</span></div>
  </div>
  <div class="photo round" role="img" aria-label="Foto: Pizza mit Tomaten und Basilikum" style="left:134px;top:12px;width:114px;height:80px;background:radial-gradient(ellipse at 50% 50%,#e4533c 0%,#d9a667 55%,#fff 72%)"></div>
  <div class="photo round" role="img" aria-label="Foto: Pizza Hawaii mit Ananas" style="left:20px;top:178px;width:101px;height:75px;background:radial-gradient(ellipse at 50% 50%,#f0c24a 0%,#de6a3b 50%,#fff 72%)"></div>
  <div class="abs" style="left:139px;top:84px;width:109px">
    <div class="item"><div class="row"><b>Hawaii</b><i>€ 14,90</i></div><span>Tomatensauce, Mozzarella, Schinken, frische Ananas, Basilikum, Olivenöl</span></div>
    <div class="item"><div class="row"><b>Capricciosa</b><i>€ 15,50</i></div><span>Tomatensauce, Mozzarella, Schinken Artischocken, Champignon, Basilikum</span></div>
    <div class="item"><div class="row"><b>Quattro Stagioni</b><i>€ 15,50</i></div><span>Tomatensauce, Mozzarella, Schinken, frische Champignon, Artischocken</span></div>
    <div class="item"><div class="row"><b>Diavola</b><i>€ 15,50</i></div><span>Tomatensauce, Mozzarella, scharfe Salami, Nduja, Pfefferoni</span></div>
    <div class="item"><div class="row"><b>La Piccante</b><i>€ 15,50</i></div><span>Tomatensauce, Mozzarella, scharfe Salami, Nduja, Pepperonata</span></div>
    <div class="item"><div class="row"><b>Primavera</b><i>€ 14,50</i></div><span>Tomatensauce, Mozzarella, Rucola, frische Tomaten, Frischkäse</span></div>
    <div class="item"><div class="row"><b>Vegetariana</b><i>€ 14,50</i></div><span>Tomatensauce, Mozzarella, Mais, Artischocken, Rucola</span></div>
    <div class="item"><div class="row"><b>Rustica</b><i>€ 15,90</i></div><span>Tomatensauce, Mozzarella, Tiroler Bauchspeck, Schinken, Mais</span></div>
    <div class="item"><div class="row"><b>Carne e Pesce</b><i>€ 15,50</i></div><span>Tomatensauce, Mozzarella, scharfe Salami, Thunfisch, Zwiebel</span></div>
  </div>
</section>

<!-- Seite 8: Pizze & Kids -->
<section class="page" style="left:378px;top:607px">
  <div class="frame"></div>
  <div class="abs" style="left:18px;top:15px;width:103px">
    <div class="item"><div class="row"><b>D.O.C.</b><i>€ 16,5</i></div><span>Tomatensauce, Mozzarella, Rohschinken, Rucola, frische Tomaten, Parmesanspäne</span></div>
    <div class="item"><div class="row"><b>Crudo</b><i>€ 16,5</i></div><span>Tomatensauce, Mozzarella, Rohschinken, Frischkäse, Parmesanspäne</span></div>
    <div class="item"><div class="row"><b>Siziliana</b><i>€ 15,5</i></div><span>Tomatensauce, Mozzarella, Thunfisch, Sardellen, Oliven, Zwiebel</span></div>
    <div class="item"><div class="row"><b>Quattro formaggio</b><i>€ 16,5</i></div><span>Tomatensauce, Mozzarella, Gorgonzola und noch 3 weitere Käse-Sorten</span></div>
    <div class="item"><div class="row"><b>La Bomba</b><i>€ 15,9</i></div><span>Tomatensauce, Mozzarella, scharfe Salami, Gorgonzola</span></div>
    <div class="item"><div class="row"><b>Frutti di Mare</b><i>€ 19,9</i></div><span>Tomatensauce, Mozzarella, Tintenfisch, Miesmuscheln, Garnelen</span></div>
    <div class="item"><div class="row"><b>Al Chef</b><i>€ 19,9</i></div><span>Tomatensauce, Mozzarella, Garnelen &amp; Knoblauch</span></div>
  </div>
  <div class="photo round" role="img" aria-label="Foto: Pizza mit Tomaten und Mozzarella von oben" style="left:131px;top:14px;width:118px;height:122px;background:radial-gradient(circle at 50% 50%,#e2543b 0%,#d7452f 45%,#e4b279 62%,#fff 72%)"></div>
  <div class="box-brown" style="left:14px;top:148px;width:236px;height:102px">
    <div class="abs" role="img" aria-label="Foto: Kinderpizza auf Holzbrett" style="left:4px;top:-8px;width:100px;height:104px;border-radius:50%;background:radial-gradient(circle at 50% 50%,#f0b24a 0%,#d98b3a 50%,#a36b3d 68%,rgba(107,83,67,0) 72%)"></div>
    <div class="abs" style="left:122px;top:8px;color:var(--yellow);font-size:14px;font-weight:700">KIDS</div>
    <div class="abs" style="left:122px;top:29px;width:106px;font-size:4.6px;line-height:1.75">
      <div class="row"><span>Kinder-Pizza - TONI - Margherita</span><span>€ 8,50</span></div>
      <div class="row"><span>Kinder-Pizza - BEN - mit Schinken</span><span>€ 9,50</span></div>
      <div class="row"><span>Kinder-Pizza - LISI - mit Salami</span><span>€ 9,50</span></div>
      <div style="font-size:3.2px;line-height:1.3;margin-top:3px">Zusätzliche Beläge 0,80 - 3,50 | Halb/Halb Belegung ist leider nicht möglich!</div>
      <div style="font-size:3.2px;line-height:1.3;margin-top:3px">Aufgrund der verschiedenen Küchenbereiche ist es nicht immer möglich, normale Gerichte und Pizze gleichzeitig zu servieren.</div>
      <div style="font-size:4.2px;color:var(--yellow);margin-top:3px">Vielen Dank für Ihr Verständnis!</div>
    </div>
  </div>
</section>

<!-- Seite 9: Kinderkarte -->
<section class="page" style="left:657px;top:607px">
  <div class="frame"></div>
  <h2 class="abs rule" style="left:18px;right:18px;top:16px;text-align:center">Toni &amp; Lisi empfehlen</h2>
  <div class="kid" style="left:58px;top:40px"><b>Feuerwehrteller „Flo“</b><span>Schnitzel mit Pommes</span><span>€ 9,90</span></div>
  <div class="kid" style="left:136px;top:40px"><b>Kinder Burger</b><span>Burger Patty vom Rind mit Cheddarkäse Salatblatt &amp; Pomme</span><span>€ 11,50</span></div>
  <div class="kid" style="left:58px;top:88px"><b>Chicken Sticks</b><span>mit Pommes</span><span>€ 9,90</span></div>
  <div class="kid" style="left:136px;top:88px"><b>Kater Moritz</b><span>Mundgerechte Pasta mit Sauce Bolognese</span><span>€ 9,50</span></div>
  <div class="kid" style="left:58px;top:136px"><b>Rotes Monster</b><span>Mundgerechte Pasta mit Tomatensauce</span><span>€ 8,50</span></div>
  <div class="kid" style="left:136px;top:136px"><b>Pommes Män</b><span>Portion Pommes mit Ketchup &amp; Mayo</span><span>€ 6,90</span></div>
  <div class="kid" style="left:58px;top:184px"><b>Räuberteller</b><span>Leerer Teller zum Mitnaschen</span><span>€ 0,00</span></div>
  <div class="kid" style="left:136px;top:184px"><b>..und dazu eine Bergquell Limo</b><span>Bubble Gum / Lemon / Peach</span><span>€ 4,30</span></div>
  <div class="fig" role="img" aria-label="Illustration: Feuerwehrmann-Figur" style="left:18px;top:40px;width:36px;height:42px;background:#f3d34a"></div>
  <div class="fig" role="img" aria-label="Illustration: Burger-Figur" style="left:212px;top:40px;width:36px;height:42px;background:#c98a3e"></div>
  <div class="fig" role="img" aria-label="Illustration: Hühnchen-Figur" style="left:14px;top:90px;width:40px;height:36px;background:#f4cf3c"></div>
  <div class="fig" role="img" aria-label="Illustration: Katze mit Pasta" style="left:212px;top:90px;width:38px;height:38px;background:#f0a23a"></div>
  <div class="fig" role="img" aria-label="Illustration: rotes Monster mit Pasta" style="left:14px;top:137px;width:40px;height:40px;background:#d9352f"></div>
  <div class="fig" role="img" aria-label="Illustration: Pommes-Figur" style="left:212px;top:134px;width:38px;height:44px;background:#e9c63a"></div>
  <div class="fig" role="img" aria-label="Illustration: Räuberfiguren auf Schlitten" style="left:10px;top:184px;width:45px;height:42px;background:#c84a3a"></div>
  <div class="abs" role="img" aria-label="Foto: drei Limonadendosen" style="left:212px;top:180px;width:53px;height:85px;border-radius:10px 0 0 0;background:linear-gradient(100deg,#f3c9a0 0%,#f5d34a 40%,#f1a1c4 75%,#e8e8ef 100%)"></div>
</section>

<!-- Seite 10: Dessert -->
<section class="page dessert" style="left:98px;top:885px">
  <div class="frame"></div>
  <h2 class="abs rule" style="left:24px;right:24px;top:16px;text-align:center">Dessert</h2>
  <div class="abs" style="left:24px;top:40px;width:92px">
    <div class="item"><b>Wein-Nudeln</b><span>Gebackene Grieß-Nudel in warmem Glühwein dazu leckeres Bratapfel-Eis</span><i>€ 9,90</i></div>
    <div class="item"><b>Helles &amp; dunkles Schokoladenmousse</b><span>mit Himbeersauce &amp; Salz-Karamell-Eis</span><i>€ 9,90</i></div>
    <div class="item"><b>Kokosnuss-Eis</b><span>in der Schale serviert 8,90 Softeis Vanille / Erdbeere / Sternchen</span><i>€ 3,20</i></div>
    <div class="item"><b>Creme Brûlée</b><span>Kirsch-Crumble &amp; Sauerrahm-Eis</span><i>€ 9,90</i></div>
    <div class="item"><b>Hausgemachtes Tiramisu</b><span>italienische Köstlichkeit</span><i>€ 9,90</i></div>
    <div class="item"><b>Schatzkiste</b><span>Vanille, Schokolade in der Schatztruhe mit Spielzeug</span><i>€ 5,50</i></div>
    <div class="item"><b>Zitronensorbet</b><span>in der Schale serviert</span><i>€ 8,90</i></div>
    <div class="item"><b>Gemischtes Eis (3 Kugeln)</b><span>Vanille, Erdbeere, Schokolade mit oder ohne Sahne</span><i>€ 5,40 / € 6,40</i></div>
  </div>
  <div class="abs" style="left:141px;top:40px;width:104px">
    <div class="item"><b>Heiße Liebe</b><span>Cremiges Vanilleeis mit heißen Himbeeren und Sahne</span><i>€ 8,50</i></div>
    <div class="item"><b>Coupe Danmark</b><span>Vanilleeis mit heißer Schokosauce und Sahne</span><i>€ 8,50</i></div>
    <div class="item"><b>Kindereisbecher mit Schokolinsen</b><span>Vanille- und Erdbeereis, Sahne und einer kleinen Überraschung</span><i>€ 9,90</i></div>
    <div class="item"><b>Softeis</b><span>Vanille / Erdbeere / Sternchen</span><i>€ 3,20</i></div>
  </div>
  <div class="abs" role="img" aria-label="Foto: Zitroneneis und Softeis-Waffeln" style="left:120px;top:145px;width:145px;height:120px;border-radius:50% 0 0 0;background:radial-gradient(ellipse at 25% 55%,#f1e27a 0%,#e8d57a 25%,rgba(255,255,255,0) 45%),radial-gradient(ellipse at 80% 40%,#f2b6c0 0%,#6b3f2c 50%,#fff 75%)"></div>
  <div class="abs" style="left:120px;top:250px;width:74px;height:15px;background:var(--red);color:#fff;font-size:5px;line-height:15px;text-align:center;border-radius:6px 6px 0 0">Alle Preise inkl. MwSt.</div>
</section>

<!-- Seite 11: Getränke -->
<section class="page" style="left:378px;top:885px">
  <div class="frame"></div>
  <h2 class="abs rule" style="left:24px;top:16px;width:102px">Spirituosen</h2>
  <div class="abs" style="left:24px;top:40px;width:102px">
    <div class="item"><b>Lorem ipsum</b><span>Lorem ipsum dolor sit amet, consectetur adipiscing elit,</span><i>€ 9,90</i></div>
    <div class="item"><b>Lorem ipsum</b><span>Lorem ipsum dolor sit amet, consectetur adipiscing elit,</span><i>€ 9,90</i></div>
    <div class="item"><b>Lorem ipsum</b><span>Lorem ipsum dolor sit amet, consectetur adipiscing elit,</span><i>€ 9,90</i></div>
    <div class="item"><b>Lorem ipsum</b><span>Lorem ipsum dolor sit amet, consectetur adipiscing elit,</span><i>€ 9,90</i></div>
    <div class="item"><b>Lorem ipsum</b><span>Lorem ipsum dolor sit amet, consectetur adipiscing elit,</span><i>€ 9,90</i></div>
  </div>
  <div class="box-red" style="left:134px;top:12px;width:118px;height:134px;padding:6px 10px">
    <h2 class="rule" style="color:#fff;border-color:#fff">Lengdrink</h2>
    <div class="item"><b>Lorem ipsum</b><span>Lorem ipsum dolor sit amet, consectetur</span><i>€ 9,90</i></div>
    <div class="item"><b>Lorem ipsum</b><span>Lorem ipsum dolor sit amet, consectetur</span><i>€ 9,90</i></div>
    <div class="item"><b>Lorem ipsum</b><span>Lorem ipsum dolor sit amet, consectetur</span><i>€ 9,90</i></div>
    <div class="item"><b>Lorem ipsum</b><span>Lorem ipsum dolor sit amet, consectetur</span><i>€ 9,90</i></div>
    <div class="item"><b>Lorem ipsum</b><span>Lorem ipsum dolor sit amet, consectetur</span><i>€ 9,90</i></div>
  </div>
  <h2 class="abs rule" style="left:144px;top:152px;width:102px">Wein</h2>
  <div class="abs" style="left:144px;top:175px;width:102px">
    <div class="item"><b>Lorem ipsum</b><span>Lorem ipsum dolor sit amet, consectetur</span><i>€ 9,90</i></div>
    <div class="item"><b>Lorem ipsum</b><span>Lorem ipsum dolor sit amet, consectetur</span><i>€ 9,90</i></div>
    <div class="item"><b>Lorem ipsum</b><span>Lorem ipsum dolor sit amet, consectetur</span><i>€ 9,90</i></div>
    <div class="item"><b>Lorem ipsum</b><span>Lorem ipsum dolor sit amet, consectetur</span><i>€ 9,90</i></div>
  </div>
  <div class="abs" role="img" aria-label="Foto: Rotweinglas, Karaffe und Whiskyglas" style="left:14px;top:160px;width:118px;height:95px;border-radius:10px;background:linear-gradient(90deg,rgba(255,255,255,0) 0%,#b6222a 18%,#eaeaea 30%,#d4943a 50%,#eaeaea 68%,#c8893a 85%,rgba(255,255,255,0) 100%);opacity:.85"></div>
</section>

<!-- Seite 12: Hotel -->
<section class="page" style="left:657px;top:885px">
  <div class="abs" role="img" aria-label="Foto: Hotel in verschneiter Berglandschaft mit Tannen" style="inset:0;background:linear-gradient(180deg,#3d6fb4 0%,#8fb3d9 22%,#e8eef4 38%,#27452f 60%,#dfe3e7 78%,#9aa3ad 100%)"></div>
  <div class="abs" style="left:56px;top:22px;color:#fff;font-size:18px;letter-spacing:.5px">ALMA'S</div>
  <div class="abs" style="left:142px;top:0;width:123px;height:47px;background:var(--red);padding:6px 7px;color:#fff">
    <div style="font-style:italic;font-weight:700;font-size:11px;line-height:1.1">APART-HOTEL</div>
    <div style="font-size:4.3px;line-height:1.3">Ihr zweites Zuhause direkt an der<br>PisteKomfortabel • Ideal für Familien<br>Wellness der Extraklasse</div>
  </div>
  <div class="abs round" role="img" aria-label="Foto: Restaurant-Stube" style="left:24px;top:190px;width:70px;height:70px;border:2px solid #fff;background:radial-gradient(circle,#c9a27a 0%,#6b4a36 70%)"></div>
  <div class="abs round" role="img" aria-label="Foto: Hallenbad im Wellnessbereich" style="left:97px;top:190px;width:70px;height:70px;border:2px solid #fff;background:radial-gradient(circle,#7fd3f2 0%,#1e6fb0 70%)"></div>
  <div class="abs round" role="img" aria-label="Foto: Ruheraum mit Sitzbereich" style="left:170px;top:190px;width:70px;height:70px;border:2px solid #fff;background:radial-gradient(circle,#b9a89a 0%,#4e4038 70%)"></div>
</section>

</body>
</html>
```